Showroom Quote Web Application - Prism Layout wanted

This web app is an internal application that will be used by one of our customers to build quotes and produce orders of retail items with their customers

the overall design should use the colour pallet provided and have a clean and simple interface

we'd like to go with a prism layout type of look

attached mockups are just a rough stab at some layouts to give you an example, please feel free to reach out with any questions.

Please don't get hung up on the specific pages, they were intended to provide context, we are looking for a high level design using the provided colour schemes and fonts, additional work may follow for the selected designer when it comes to specific pages or work flows.

Sorry for the short timeline, we have a tight deadline on this one.

Target Market(s)

internal application for customer

Industry/Entity Type

Retail

Other font styles liked:
• see attached doc for fonts

Requirements
Must have
• simple and clean interface
• intuitive design
Nice to have
• see attached documents for logo colour schemes and fonts
• these must be incorporated into the design

```html
<!DOCTYPE html>
<html lang="en">
<head>
<meta charset="utf-8">
<title>Prism Layout – New Customer</title>
<link rel="stylesheet" href="https://fonts.googleapis.com/css2?family=Lato:wght@400;700&family=Source+Sans+3:wght@300;400;700&display=swap">
<style>
  :root {
    --bg: #0b3a7b;
    --prism-dark: #083069;
    --prism-mid: #0a3574;
    --white: #ffffff;
    --field-line: rgba(255,255,255,0.85);
    --friendloop: #4e69a2;
    --chirpline: #0099ef;
    --orbitnet: #d73d32;
    --cta-text: #0b3a7c;
  }
  * { box-sizing: border-box; margin: 0; padding: 0; }
  html, body { width: 675px; height: 1200px; overflow: hidden; }
  body {
    position: relative;
    background: var(--bg);
    color: var(--white);
    font-family: "Source Sans 3", "Helvetica Neue", Arial, sans-serif;
  }
  .prism-backdrop { position: absolute; inset: 0; width: 675px; height: 1200px; }

  .status-bar {
    position: absolute; top: 0; left: 0; width: 675px; height: 36px;
    display: flex; align-items: center; justify-content: space-between;
    padding: 0 12px; font-size: 19px; font-family: "Source Sans 3", Arial, sans-serif;
  }
  .status-left, .status-right { display: flex; align-items: center; gap: 6px; width: 200px; }
  .status-right { justify-content: flex-end; }
  .status-time { font-weight: 700; font-size: 20px; }
  .signal { display: flex; gap: 3px; }
  .signal span { width: 10px; height: 10px; border-radius: 50%; border: 1.3px solid var(--white); }
  .signal span.on { background: var(--white); }
  .battery { width: 40px; height: 17px; border: 1.5px solid var(--white); border-radius: 3px; padding: 2px; position: relative; }
  .battery::after { content: ""; position: absolute; right: -5px; top: 4px; width: 3px; height: 6px; background: var(--white); border-radius: 0 2px 2px 0; }
  .battery-level { width: 22%; height: 100%; background: var(--white); border-radius: 1px; }

  .form-title {
    position: absolute; top: 122px; left: 0; width: 675px; text-align: center;
    font-weight: 300; font-size: 26px; letter-spacing: 0.1px;
  }

  .field {
    position: absolute; left: 123px; width: 430px; height: 80px;
    border: 1.2px solid var(--field-line); border-radius: 4px;
    display: flex; align-items: center; justify-content: space-between;
    padding: 0 24px 0 29px; font-weight: 300; font-size: 23px;
  }
  .field svg { width: 26px; height: 26px; fill: none; stroke: var(--white); stroke-width: 1.3; }

  .social-button {
    position: absolute; left: 123px; width: 432px; height: 72px; border-radius: 3px;
    display: flex; align-items: center; font-family: "Lato", Arial, sans-serif;
    font-size: 19px; font-weight: 400; color: var(--white);
  }
  .social-button .marker { width: 16px; height: 16px; border-radius: 50%; background: var(--white); margin: 0 29px 0 31px; }
  .social-friendloop { top: 722px; background: var(--friendloop); }
  .social-chirpline { top: 802px; background: var(--chirpline); }
  .social-orbitnet { top: 883px; background: var(--orbitnet); }

  .continue-button {
    position: absolute; top: 996px; left: 123px; width: 430px; height: 101px;
    background: var(--white); border-radius: 4px;
    display: flex; align-items: center; justify-content: center;
    color: var(--cta-text); font-weight: 700; font-size: 31px; letter-spacing: 0.3px;
  }
</style>
</head>
<body>
  <svg class="prism-backdrop" viewBox="0 0 675 1200" aria-hidden="true">
    <polygon points="675,320 675,560 60,780 0,760 0,700" fill="var(--prism-mid)"/>
    <polygon points="0,460 0,700 180,620" fill="var(--prism-dark)"/>
    <polygon points="55,780 675,560 675,900 320,1030" fill="var(--prism-mid)"/>
    <polygon points="0,800 55,780 420,1200 0,1200" fill="var(--prism-dark)" opacity="0.7"/>
    <polygon points="560,1080 675,1050 675,1200 600,1200" fill="var(--prism-dark)"/>
  </svg>

  <header class="status-bar">
    <div class="status-left">
      <div class="signal"><span class="on"></span><span class="on"></span><span class="on"></span><span></span><span></span></div>
      <span class="carrier">KESTREL</span>
      <svg width="20" height="15" viewBox="0 0 20 15" aria-label="Wi-Fi"><path d="M10 14 L6.5 10.3 A5 5 0 0 1 13.5 10.3 Z" fill="#fff"/><path d="M3.5 7.3 A9 9 0 0 1 16.5 7.3" stroke="#fff" stroke-width="2" fill="none"/><path d="M0.8 4.4 A13 13 0 0 1 19.2 4.4" stroke="#fff" stroke-width="2" fill="none"/></svg>
    </div>
    <span class="status-time">4:21 PM</span>
    <div class="status-right">
      <span>22%</span>
      <div class="battery"><div class="battery-level"></div></div>
    </div>
  </header>

  <h1 class="form-title">Please fill out the new customer’s information</h1>

  <div class="field" style="top:197px"><span>Name</span>
    <svg viewBox="0 0 26 26"><circle cx="13" cy="8.5" r="5"/><path d="M3.5 22 C4 16 8 14 13 14 C18 14 22 16 22.5 22 Z"/></svg></div>
  <div class="field" style="top:296px"><span>Address</span>
    <svg viewBox="0 0 26 26" style="height:30px"><path d="M13 25 C7 17 4.5 13 4.5 9.5 A8.5 8.5 0 0 1 21.5 9.5 C21.5 13 19 17 13 25 Z"/><circle cx="13" cy="9.5" r="2.8"/></svg></div>
  <div class="field" style="top:395px"><span>Phone</span>
    <svg viewBox="0 0 26 26"><path d="M6 3 L9.5 7.5 L7.5 10 C9 13.5 12 16.5 15.5 18 L18 16 L22.5 19.5 L20 23 C12 22.5 3.5 14 3 6 Z"/></svg></div>
  <div class="field" style="top:494px"><span>Cell</span>
    <svg viewBox="0 0 26 26"><path d="M6 3 L9.5 7.5 L7.5 10 C9 13.5 12 16.5 15.5 18 L18 16 L22.5 19.5 L20 23 C12 22.5 3.5 14 3 6 Z"/></svg></div>
  <div class="field" style="top:593px"><span>Email</span>
    <svg viewBox="0 0 30 22" style="width:30px;height:22px"><rect x="1" y="1.5" width="28" height="19"/><path d="M1 1.5 L15 13 L29 1.5 M1 20.5 L11.5 10 M29 20.5 L18.5 10"/></svg></div>

  <div class="social-button social-friendloop"><span class="marker"></span>Login with your Friendloop</div>
  <div class="social-button social-chirpline"><span class="marker"></span>Login with your Chirpline</div>
  <div class="social-button social-orbitnet"><span class="marker"></span>Login with your Orbitnet</div>

  <div class="continue-button">CONTINUE</div>
</body>
</html>
```